Fahrzeugbeschriftung für Informationselektronik
Zielgruppe
SAT-Anlagen, Antennenanlagen, Kabelfernsehen
Telekommunikation, Internet, Netzwerktechnik
Radio- und Fernsehtechnik
Alarmanlagen, Videoüberwachung
Elektrokleinreparaturen
Zielgruppe: Hauptsächlich Privatleute
Beratung, Planung, Neuinstallation und hauptsächlich Service und Reparaturen
Aufgabenstellung
auffällig, anders nicht nur Schrift und Logo fertig
WALDEK Informationselektronik
Master Professional

```html
<!DOCTYPE html>
<html lang="de">
<head>
<meta charset="utf-8">
<title>WALDEK Informationstechnik – Fahrzeugbeschriftung</title>
<link rel="stylesheet" href="https://fonts.googleapis.com/css2?family=Saira+Semi+Condensed:wght@500;600;700&display=swap">
<style>
  :root {
    --panel-white: #ffffff;
    --panel-grey: #c9ccd2;
    --tech-blue: #4f7fd0;
    --tech-deep: #1d3566;
    --tech-night: #14213f;
    --glow-orange: #d9782f;
    --ink-dark: #3a3d44;
    --ink-light: #ffffff;
    --shadow-dark: rgba(10, 16, 34, 0.85);
    --page-bg: #f2f3f5;
  }
  * { margin: 0; padding: 0; box-sizing: border-box; }
  html, body {
    width: 1200px; height: 524px; overflow: hidden;
    background: var(--page-bg);
    font-family: "Saira Semi Condensed", "Arial Narrow", sans-serif;
  }
  .wrap-design {
    position: relative; width: 1200px; height: 524px; overflow: hidden;
  }
  .network-visual {
    position: absolute; inset: 0;
    background:
      radial-gradient(ellipse 320px 220px at 900px 170px, rgba(217,120,47,0.55), transparent 70%),
      radial-gradient(ellipse 260px 180px at 1080px 330px, rgba(217,120,47,0.35), transparent 70%),
      linear-gradient(90deg, var(--panel-white) 0%, var(--panel-grey) 24%, var(--tech-blue) 42%, var(--tech-deep) 68%, var(--tech-night) 100%);
  }
  .company-address {
    position: absolute; left: 60px; top: 190px;
    color: var(--ink-dark); font-weight: 500; font-size: 15px; line-height: 21px;
  }
  .brand {
    position: absolute; left: 600px; top: 20px; color: var(--ink-light);
  }
  .brand-name {
    display: flex; align-items: center; gap: 16px;
    font-weight: 700; font-size: 104px; line-height: 1; letter-spacing: 2px;
  }
  .brand-dot {
    width: 26px; height: 26px; border-radius: 50%; background: var(--ink-light);
  }
  .brand-field {
    font-weight: 700; font-size: 38px; line-height: 1.1; letter-spacing: 1px; margin-left: 42px;
  }
  .brand-title {
    position: absolute; left: 880px; top: 178px;
    color: var(--ink-light); font-weight: 600; font-size: 30px; letter-spacing: 1px;
  }
  .contact-line {
    position: absolute; top: 232px; left: 320px; right: 40px;
    display: flex; justify-content: space-between;
    color: var(--ink-light); font-weight: 600; font-size: 38px;
    text-shadow: 2px 2px 0 var(--shadow-dark);
  }
  .service-list {
    position: absolute; list-style: none;
    color: var(--ink-light); font-weight: 600; font-size: 20px; line-height: 29px;
    text-shadow: 1px 1px 0 var(--shadow-dark);
  }
  .service-list--left { left: 250px; top: 288px; }
  .service-list--right { left: 660px; top: 284px; }
  .service-list li::before { content: "- "; }
  .claim {
    position: absolute; left: 160px; top: 378px;
    color: var(--ink-light); font-weight: 600; font-size: 32px; letter-spacing: 0.5px;
    text-shadow: 2px 2px 0 var(--shadow-dark);
  }
  .claim-divider { margin: 0 14px; }
</style>
</head>
<body>
<main class="wrap-design">
  <div class="network-visual" role="img" aria-label="Hintergrundbild: digitales Netzwerk mit leuchtenden Verbindungslinien und Lichtpunkten in Blau und Orange"></div>

  <address class="company-address">
    INFORMATIONSTECHNIK WALDEK<br>
    Meisterbetrieb<br>
    Lindenweg 42,<br>
    D-50389 Wesseling
  </address>

  <div class="brand">
    <div class="brand-name"><span>WALDEK</span><span class="brand-dot"></span></div>
    <div class="brand-field">INFORMATIONSTECHNIK</div>
  </div>
  <div class="brand-title">Meisterbetrieb</div>

  <div class="contact-line">
    <span class="contact-web">www.waldek-info.de</span>
    <span class="contact-phone">mob. (0172) 61 93 207</span>
  </div>

  <ul class="service-list service-list--left">
    <li>Sat-Kabel-Antennentechnik</li>
    <li>Alarm- &amp; Sicherheitstechnik</li>
    <li>Daten- &amp; Netzwerktechnik</li>
  </ul>
  <ul class="service-list service-list--right">
    <li>Gebäudekommunikation</li>
    <li>Unterhaltungselektronik</li>
    <li>Videoüberwachung</li>
  </ul>

  <p class="claim">BERATUNG<span class="claim-divider">|</span>VERKAUF<span class="claim-divider">|</span>MONTAGE<span class="claim-divider">|</span>SERVICE</p>
</main>
</body>
</html>
```